Clean Stylish Hip Online Marketplace Website Design

I am needing a seasoned designer with a hipster flair to design an online marketplace that connects people with others who can provide home and professional baking services in their local area. Need maps, feature driven and above all an identifiable LOOK to the site that is clean, trustworthy and inviting. (Online Marketplace service like Quillrest, Tamblo.com, CraftHerdz but with the look of Wanderlattebook.com, Zipo, holbeckinn.com)

Target Market(s)

Women, special occasion hosts, Moms, Bride-to-be

Industry/Entity Type

Marketplace

Number of Pages Required

5+ page

Font styles to use
Serif
Sans Serif

Requirements
Must have
• Modern, subtle feminine elements, hip. 2 options for user on home page similar to craft herdz 1) Become a OvenNest 2) Post or Search For Your Dessert. ABOUT, Categories (list of baked goods), Browse Projects, How it works, Log in. Profile set up page and profile of bakers with their uploaded photos of their baked items. Post for a project page where user can go it in request all bakers in the area for a baked good. Name, City Baked good,Date/Time needed, Description of Project and submit button. List of all the projects where bakers can accept or decline project with a bid. Payment Page.
Nice to have
• Map capabilities somewhere for people to filter down by location. Be able to showcase bakers cake or cookies photos in a beautiful unique and stylish way.
Should not have
• Nothing too girly or corporate. I am looking for a very stylized website for an online marketplace.

```html
<!DOCTYPE html>
<html lang="en">
<head>
<meta charset="utf-8">
<title>OvenNest – Become a Baker</title>
<link rel="stylesheet" href="https://fonts.googleapis.com/css2?family=Montserrat:wght@400;500;700&family=Roboto:wght@300;400;500&display=swap">
<style>
:root{
  --pink:#e8146b;
  --orange:#ff8c3c;
  --plum:#8e6a93;
  --ink:#2b2b2b;
  --text:#555;
  --rule:#e6e6e6;
  --footer:#e9ecef;
  --slate:#d3dae1;
  --green:#3fa83a;
  --gold:#e2b418;
}
*{box-sizing:border-box;margin:0;padding:0}
html,body{width:1200px;height:965px;overflow:hidden;background:#fff}
body{position:relative;font-family:'Roboto',sans-serif;color:var(--ink)}
.abs{position:absolute}

.site-header{position:absolute;left:0;top:0;width:1200px;height:88px;background:#fff;box-shadow:0 2px 6px rgba(0,0,0,.08)}
.brand{left:97px;top:24px;font-family:'Roboto',sans-serif;font-size:29px;font-weight:400;letter-spacing:.5px;color:#222}
.nav a{position:absolute;top:34px;font-size:16px;color:#333;text-decoration:none}
.btn-login{left:1013px;top:27px;width:88px;height:36px;background:var(--orange);color:#fff;border-radius:2px;font-size:16px;font-weight:500;display:flex;align-items:center;justify-content:center}

.page-title{left:96px;top:118px;font-family:'Montserrat',sans-serif;font-weight:700;font-size:42px;color:var(--pink);letter-spacing:-.3px}
.page-sub{left:97px;top:171px;font-family:'Montserrat',sans-serif;font-weight:400;font-size:22px;color:var(--orange)}

.status{left:1005px;top:137px;font-size:13px;color:#999;font-family:'Montserrat',sans-serif}
.toggle{left:1053px;top:134px;width:48px;height:22px;border:2px solid var(--green);border-radius:4px;background:#fff}
.toggle .on{position:absolute;left:0;top:0;width:20px;height:18px;background:var(--green)}

.portrait{left:104px;top:234px;width:316px;height:316px;border-radius:50%;border:2px solid var(--plum);padding:6px}
.portrait .photo{width:100%;height:100%;border-radius:50%;background:radial-gradient(circle at 45% 40%,#6b8bbf 0,#4b69a3 25%,#a4866c 55%,#e0d2c4 100%)}
.connector{left:420px;top:391px;width:150px;height:2px;background:var(--plum)}
.connector-dot{left:567px;top:387px;width:9px;height:9px;border-radius:50%;background:var(--plum)}

.btn{position:absolute;top:604px;height:42px;display:flex;align-items:center;justify-content:center;font-family:'Montserrat',sans-serif;font-weight:700;font-size:14px;border-radius:2px}
.btn-solid{left:99px;width:126px;background:var(--orange);color:#fff}
.btn-outline{left:245px;width:314px;border:2px solid var(--orange);color:var(--orange)}

.ribbon{left:626px;top:232px}
.ribbon-text{left:640px;top:242px;font-family:'Montserrat',sans-serif;font-size:20px;color:#fff}
.bio{left:630px;top:290px;width:474px;font-size:12px;line-height:22px;color:var(--text)}
.meta{left:630px;top:368px;display:flex;align-items:center;font-size:12px;color:#444}
.meta .sep{margin:0 18px;color:#777}
.meta svg{margin-right:7px}
.rule{height:1px;background:var(--rule);left:630px;width:467px}
.spec-title{left:631px;top:419px;font-family:'Montserrat',sans-serif;font-weight:700;font-size:16px}
.spec{position:absolute;top:463px;width:94px;height:94px;border-radius:50%;border:2px solid var(--pink);padding:4px}
.spec .disc{width:100%;height:100%;border-radius:50%;background:var(--pink);display:flex;align-items:center;justify-content:center}
.permit{left:631px;font-family:'Montserrat',sans-serif;font-weight:700;font-size:15px}
.permit span{font-family:'Roboto',sans-serif;font-weight:400;color:#555}
.permit .yes{color:var(--plum);font-weight:500}

.gallery-arrow{top:694px;width:27px;height:162px;background:var(--slate);display:flex;align-items:center;justify-content:center}
.shot{top:694px;width:173px;height:162px}

.site-footer{left:0;top:912px;width:1200px;height:53px;background:var(--footer)}
.copy{left:99px;top:933px;font-family:'Montserrat',sans-serif;font-size:12px;color:#222}
.social{top:926px;width:27px;height:27px;border-radius:50%;border:1.5px solid #b9bfc6}
.pagecode{left:1143px;top:933px;font-size:12px;color:#222;font-family:'Montserrat',sans-serif}
</style>
</head>
<body>

<header class="site-header">
  <div class="abs brand">OVENNEST</div>
  <nav class="nav">
    <a style="left:475px">About us</a>
    <a style="left:587px">Categories</a>
    <a style="left:711px">Browse Projects</a>
    <a style="left:874px">How it Works</a>
  </nav>
  <div class="abs btn-login">LOG IN</div>
</header>

<h1 class="abs page-title">BECOME A OVENNEST</h1>
<p class="abs page-sub">Setup Profile Information</p>

<div class="abs status">Active</div>
<div class="abs toggle"><div class="on"><svg width="20" height="18" viewBox="0 0 20 18"><path d="M5 9l3.5 3.5L15 5.5" stroke="#fff" stroke-width="2.4" fill="none"/></svg></div>
  <svg class="abs" style="left:26px;top:5px" width="12" height="9"><path d="M2 0v9M6 0v9M10 0v9" stroke="#ccc" stroke-width="1"/></svg>
</div>

<div class="abs portrait"><div class="photo" role="img" aria-label="Baker in a blue top and apron arranging chocolate cupcakes on a stand"></div></div>
<div class="abs connector"></div>
<div class="abs connector-dot"></div>

<div class="btn btn-solid">NUT FREE</div>
<div class="btn btn-outline">UPLOAD PHOTOS OF BAKED GOODS</div>

<svg class="abs ribbon" width="399" height="43"><polygon points="0,0 399,0 365,43 0,43" fill="#ff8c3c"/></svg>
<div class="abs ribbon-text">FINIBUS BONORUM ET MALORUM</div>
<p class="abs bio">Sed ut perspiciatis unde omnis iste natus error sit voluptatem accusantium doloremque laudantium, totam rem aperiam, eaque ipsa quae ab illo inventore veritatis et quasi archi-tecto beatae vitae dicta sunt explicabo. Nemo enim ipsam voluptatem quia</p>

<div class="abs meta">
  <svg width="11" height="11" viewBox="0 0 11 11"><rect x=".5" y="1.5" width="10" height="9" fill="none" stroke="#555"/><path d="M.5 4h10M3 0v3M8 0v3M3 6h1M6 6h1M3 8h1M6 8h1" stroke="#555"/></svg>7 YEARS
  <span class="sep">|</span>
  <svg width="80" height="12" viewBox="0 0 80 12" style="margin-right:0">
    <g fill="#e2b418"><path id="st" d="M6 0l1.8 3.8 4.2.5-3.1 2.9.8 4.1L6 9.3 2.3 11.3l.8-4.1L0 4.3l4.2-.5z"/><use href="#st" x="14"/><use href="#st" x="28"/><use href="#st" x="42"/><use href="#st" x="56"/></g>
  </svg>
  <span class="sep">|</span>
  <svg width="8" height="11" viewBox="0 0 8 11"><path d="M4 0a4 4 0 0 1 4 4c0 3-4 7-4 7S0 7 0 4a4 4 0 0 1 4-4z" fill="#555"/><circle cx="4" cy="4" r="1.5" fill="#fff"/></svg>natus error sit&nbsp; accusantium
</div>

<div class="abs rule" style="top:403px"></div>
<h2 class="abs spec-title">Specialties In :</h2>

<svg class="abs" style="left:632px;top:500px" width="12" height="20"><path d="M10 1L2 10l8 9" stroke="#8a97a3" stroke-width="1.5" fill="none"/></svg>
<div class="spec" style="left:657px"><div class="disc">
  <svg width="40" height="42" viewBox="0 0 40 42" fill="#fff"><path d="M20 2c3 0 4 3 3 5 5 0 8 4 6 8 4 1 5 5 3 8H8c-2-3-1-7 3-8-2-4 1-8 6-8-1-2 0-5 3-5z"/><path d="M6 26h28l-4 14H10z"/></svg></div></div>
<div class="spec" style="left:773px"><div class="disc">
  <svg width="40" height="42" viewBox="0 0 40 42" fill="#fff"><path d="M10 8v8M17 8v8M23 8v8M30 8v8" stroke="#fff" stroke-width="2"/><path d="M4 18h32v22H4z"/><path d="M4 27c5-5 8 5 13 0s8 5 13 0 4-3 6-2" stroke="#e8146b" stroke-width="2" fill="none"/></svg></div></div>
<div class="spec" style="left:889px"><div class="disc">
  <svg width="44" height="34" viewBox="0 0 44 34" fill="#fff"><path d="M2 18C2 8 12 2 22 2s20 6 20 16z"/><path d="M2 21h40l-3 12H5z"/><circle cx="13" cy="12" r="2" fill="#e8146b"/><circle cx="22" cy="9" r="2" fill="#e8146b"/><circle cx="31" cy="12" r="2" fill="#e8146b"/></svg></div></div>
<div class="spec" style="left:1005px"><div class="disc">
  <svg width="44" height="44" viewBox="0 0 44 44"><circle cx="22" cy="22" r="20" fill="#fff"/><circle cx="22" cy="22" r="6" fill="#e8146b"/><path d="M8 28c4 4 6 0 9 4s6 2 8-1 6 2 9-3" stroke="#e8146b" stroke-width="3" fill="none"/></svg></div></div>
<svg class="abs" style="left:1120px;top:500px" width="12" height="20"><path d="M2 1l8 9-8 9" stroke="#8a97a3" stroke-width="1.5" fill="none"/></svg>

<div class="abs rule" style="top:580px"></div>
<p class="abs permit" style="top:596px">Food Handlers Permit : <span class="yes">Yes</span><span> / No / Pending</span></p>
<p class="abs permit" style="top:631px">Business License : <span class="yes">Yes</span><span> / No / Pending</span></p>

<div class="abs gallery-arrow" style="left:100px"><svg width="14" height="42"><path d="M12 1L2 21l10 20" stroke="#7f8b97" stroke-width="1.3" fill="none"/></svg></div>
<div class="abs shot" style="left:139px;background:linear-gradient(135deg,#2a1d18,#6b4030 50,#2a1d18)" role="img" aria-label="Chocolate bars topped with halved strawberries"></div>
<div class="abs shot" style="left:327px;background:linear-gradient(160deg,#6b4a3a,#f2e3d6 55%,#d84050)" role="img" aria-label="Meringue cake layered with cream and berries"></div>
<div class="abs shot" style="left:513px;background:radial-gradient(circle at 50% 50%,#b57a3c,#e7d6c0 60%,#5b3a2a)" role="img" aria-label="Tray of frosted cupcakes with sprinkles"></div>
<div class="abs shot" style="left:701px;background:linear-gradient(135deg,#c65f1c,#e79a44 50%,#6e4426)" role="img" aria-label="Golden savoury pie cut into slices"></div>
<div class="abs shot" style="left:889px;background:radial-gradient(circle at 55% 60%,#a86a34,#d9a86a 45%,#f3d9ae)" role="img" aria-label="Chocolate chip cookies stacked on a table"></div>
<div class="abs gallery-arrow" style="left:1075px"><svg width="14" height="42"><path d="M2 1l10 20-10 20" stroke="#7f8b97" stroke-width="1.3" fill="none"/></svg></div>

<footer class="abs site-footer"></footer>
<p class="abs copy">Copyrights@2016Company Name, All rights reserved</p>
<div class="abs social" style="left:902px"></div>
<div class="abs social" style="left:936px"></div>
<div class="abs social" style="left:970px"></div>
<div class="abs social" style="left:1004px"></div>
<div class="abs social" style="left:1038px"></div>
<div class="abs social" style="left:1072px"><svg width="24" height="24" viewBox="0 0 24 24"><rect x="7" y="8.5" width="10" height="7" fill="none" stroke="#9aa1a8"/><path d="M7 8.5l5 4 5-4" fill="none" stroke="#9aa1a8"/></svg></div>
<p class="abs pagecode">C15</p>

</body>
</html>
```